Health and wellnes company needs business cards

We are a Health and wellness business just relocated to Spain. Here nobody knows our business so we would like to put some of our services on the card. Clean design with logo.

Contact Information for Business Card

Brightmeadow
Clara & Tobias Wennberg
Calle de los Almendros 17
Sanlúcar de Barrameda
Mobile: 0046 731 402768
info@brightmeadow-example.se

Font styles to use
Serif

Colors
85cae6
85acd3
b768aa

Requirements
Must have
• these Services somewhere on the card
• - Private or group yoga
• - Reconnective healing
• - Kitesurfing lessons
• - Massage
• LOgo somewhere
Nice to have
• Colours that go with the logo please

```html
<!DOCTYPE html>
<html lang="en">
<head>
<meta charset="utf-8">
<title>Brightmeadow business card</title>
<link rel="stylesheet" href="https://fonts.googleapis.com/css2?family=Marcellus&family=Poppins:wght@400&display=swap">
<style>
  :root {
    --page: #ecebe8;
    --card-white: #ffffff;
    --navy: #1b3a6b;
    --navy-deep: #142d57;
    --navy-light: #24477f;
    --teal: #5cc3c7;
    --soft-white: #dfe8f3;
    --grey-text: #5a5a5a;
  }
  * { box-sizing: border-box; margin: 0; padding: 0; }
  html, body {
    width: 1200px; height: 862px; overflow: hidden;
    background: var(--page);
  }
  .canvas { position: relative; width: 1200px; height: 862px; }

  .card {
    position: absolute; top: 154px;
    width: 317px; height: 554px;
    border-radius: 80px 0 80px 0;
    overflow: hidden;
  }
  .card--front { left: 265px; background: var(--card-white); }
  .card--back  { left: 618px; background: var(--navy); }

  .brand-dot {
    position: absolute; left: 50%; top: 102px;
    width: 58px; height: 58px; margin-left: -29px;
    border-radius: 50%; background: var(--teal);
  }
  .brand-name {
    position: absolute; left: 0; right: 0; top: 192px;
    text-align: center;
    font-family: "Marcellus", serif; font-size: 27px; font-weight: 400;
    letter-spacing: 0.5px; color: var(--navy);
  }
  .owners {
    position: absolute; left: 0; right: 0; top: 290px;
    text-align: center;
    font-family: "Marcellus", serif; font-size: 20px; line-height: 30px;
    color: var(--navy); text-transform: uppercase;
  }
  .contact {
    position: absolute; left: 0; right: 0; top: 376px;
    font-family: "Poppins", sans-serif; font-size: 13px; color: var(--grey-text);
    text-align: center;
  }
  .contact-line {
    display: flex; justify-content: center; align-items: center;
    gap: 8px; height: 20px;
  }
  .contact-icon { width: 12px; height: 12px; flex: none; }
  .divider {
    width: 18px; height: 2px; background: var(--teal);
    margin: 10px auto 9px;
  }
  .address-line { line-height: 20px; }

  .back-pattern {
    position: absolute; inset: 0;
    background:
      radial-gradient(circle at 50% 50%, var(--navy-light) 0%, transparent 70%),
      linear-gradient(180deg, var(--navy-light) 0%, var(--navy) 45%, var(--navy-deep) 100%);
  }
  .back-mark {
    position: absolute; left: 0; right: 0; top: 250px;
    display: flex; flex-direction: column; align-items: center; gap: 10px;
  }
  .back-mark .mark-dot {
    width: 44px; height: 44px; border-radius: 50%; background: var(--teal);
  }
  .back-mark .mark-name {
    font-family: "Marcellus", serif; font-size: 15px;
    letter-spacing: 0.5px; color: var(--teal);
  }
  .services {
    position: absolute; left: 0; right: 0; top: 372px;
    list-style: none; text-align: center;
    font-family: "Marcellus", serif; font-size: 14px; line-height: 24px;
    letter-spacing: 0.3px; color: var(--soft-white);
  }
  .services-divider {
    width: 18px; height: 2px; background: var(--teal);
    margin: 0 auto 10px;
  }
</style>
</head>
<body>
<main class="canvas">
  <section class="card card--front">
    <div class="brand-dot"></div>
    <h1 class="brand-name">BRIGHTMEADOW</h1>
    <p class="owners">Clara &amp;<br>Tobias Wennberg</p>
    <div class="contact">
      <p class="contact-line">
        <svg class="contact-icon" viewBox="0 0 24 24" aria-hidden="true">
          <path fill="#5cc3c7" d="M6.6 10.8a15.1 15.1 0 0 0 6.6 6.6l2.2-2.2c.3-.3.7-.4 1-.2 1.1.4 2.3.6 3.6.6.6 0 1 .4 1 1V20c0 .6-.4 1-1 1A17 17 0 0 1 3 4c0-.6.4-1 1-1h3.5c.6 0 1 .4 1 1 0 1.3.2 2.5.6 3.6.1.3 0 .7-.2 1z"/>
        </svg>
        <span>0046 731 402768</span>
      </p>
      <p class="contact-line">
        <svg class="contact-icon" viewBox="0 0 24 24" aria-hidden="true">
          <rect x="2.5" y="5" width="19" height="14" rx="1" fill="none" stroke="#5cc3c7" stroke-width="2"/>
          <path d="M3 6l9 7 9-7" fill="none" stroke="#5cc3c7" stroke-width="2"/>
        </svg>
        <span>info@brightmeadow-example.se</span>
      </p>
      <div class="divider"></div>
      <p class="address-line">Calle de los Almendros 17</p>
      <p class="address-line">Sanlúcar de Barrameda</p>
    </div>
  </section>

  <section class="card card--back">
    <div class="back-pattern" role="img" aria-label="Repeating tone-on-tone pattern of the brand symbol on navy"></div>
    <div class="back-mark">
      <div class="mark-dot"></div>
      <span class="mark-name">BRIGHTMEADOW</span>
    </div>
    <ul class="services">
      <li class="services-divider" aria-hidden="true"></li>
      <li>Private or group yoga</li>
      <li>Reconnective healing</li>
      <li>Kitesurfing lessons</li>
      <li>Massage</li>
    </ul>
  </section>
</main>
</body>
</html>
```